International Medical Company Needs a Website Design for a Support Site

We need a website design for a support site we are doing for ostomates called Bright Rebounds. We are an international company but this website is for our Australian market.

The website is a support site for people who are living with an Ostomy or Bowel Disease. This is a site where they can read other ostomates' stories and how they are dealing with the fact that they have to wear a pouch everyday.

The URL for our US site is: http://www.brightrebounds-example.com/

We need to use the same logo but we have freedom around the color scheme. We are not fond of the brown color scheme used in our US site and are happy for designs to be submitted with alternatives.

• We want the design to be clean, inspiring, modern and inviting.
• We would like to see a design for the mainpage / homepage and one of the subpages
• We only require the PSD / image files (no HTML needed)

Attached to this project is our sitemap, an example wireframe and the logos. We are happy for you to play around with different options and don't have to stick to the layout shown in the wireframe.

If you have any further questions please ask.

```html
<!DOCTYPE html>
<html lang="en">
<head>
<meta charset="utf-8">
<title>Bright Rebounds – Sharing stories and giving hope</title>
<link rel="stylesheet" href="https://fonts.googleapis.com/css2?family=Ubuntu:ital,wght@0,300;0,400;0,500;0,700;1,400&display=swap">
<style>
  :root {
    --green: #6acf4a;
    --slate: #34444f;
    --page: #ebebed;
    --header: #e2e2e4;
    --ink: #4a4a4a;
    --text: #5c5c5c;
    --muted: #777;
    --rule: #cfcfd2;
    --white: #ffffff;
  }
  * { box-sizing: border-box; margin: 0; padding: 0; }
  html, body { width: 756px; height: 1200px; overflow: hidden; background: var(--page); }
  body { font-family: "Ubuntu", sans-serif; color: var(--text); }
  .canvas { position: relative; width: 756px; height: 1200px; overflow: hidden; background: var(--page); }
  .abs { position: absolute; }

  /* Header */
  .masthead { position: absolute; left: 0; top: 0; width: 756px; height: 360px; background: var(--header); }
  .brand { position: absolute; left: 108px; top: 19px; font-size: 12px; font-weight: 500; letter-spacing: 1px; color: #6b6b6b; }
  .share-link { position: absolute; left: 300px; top: 21px; font-size: 8px; font-weight: 700; color: var(--green); }
  .field { position: absolute; top: 18px; height: 17px; background: #f4f4f5; border: 1px solid #d8d8da; font-size: 7px; font-style: italic; color: #999; padding: 4px 6px; }
  .field.country { left: 508px; width: 73px; }
  .field.search { left: 593px; width: 89px; }
  .field svg { position: absolute; right: 5px; top: 4px; }
  .nav-bar { position: absolute; left: 0; top: 47px; }
  .nav { position: absolute; top: 65px; font-size: 8.5px; color: var(--white); letter-spacing: 0.2px; }

  /* Hero */
  .hero-photo { position: absolute; left: 0; top: 100px; }
  .hero-copy { position: absolute; right: 74px; top: 248px; text-align: right; }
  .hero-title { font-size: 11px; font-weight: 500; line-height: 12px; color: #4a4a4a; }
  .hero-title .accent { color: var(--green); }
  .hero-text { margin-top: 7px; font-size: 7.6px; line-height: 9.8px; color: #666; }
  .btn { position: absolute; top: 330px; height: 15px; background: var(--green); color: var(--white); font-size: 6px; font-weight: 500; text-align: center; line-height: 15px; }
  .or { position: absolute; left: 613px; top: 332px; font-size: 8px; color: #666; }

  /* Intro band */
  .intro { position: absolute; left: 0; top: 360px; width: 756px; height: 137px; background: var(--slate); text-align: center; color: var(--white); }
  .intro h1 { position: absolute; left: 0; right: 0; top: 27px; font-size: 15.5px; font-weight: 700; }
  .intro .divider { position: absolute; left: 366px; top: 56px; width: 24px; height: 1px; background: #7c8a93; }
  .intro p { position: absolute; left: 100px; right: 100px; top: 68px; font-size: 12px; font-weight: 300; line-height: 18px; }

  /* Sections */
  .heading { position: absolute; font-size: 11.5px; font-weight: 500; color: var(--ink); }
  .heading::after { content: ""; position: absolute; left: 0; top: 23px; width: 24px; height: 1px; background: var(--rule); }
  .body { position: absolute; font-size: 7.9px; line-height: 14.2px; color: var(--text); }
  .link-green { position: absolute; font-size: 8px; font-weight: 500; color: var(--green); }
  .subhead { position: absolute; font-size: 9px; font-weight: 500; color: var(--ink); }
  .photo { position: absolute; }
  .story-name { position: absolute; font-size: 8px; font-weight: 500; color: var(--ink); line-height: 10px; }
  .story-name span { display: block; font-weight: 400; color: var(--muted); }
  .more { position: absolute; right: 74px; top: 780px; font-size: 6.8px; font-weight: 500; color: #555; }

  .article { position: absolute; width: 190px; }
  .article h3 { font-size: 9px; font-weight: 500; color: var(--ink); line-height: 11px; }
  .article .byline { font-size: 7.4px; font-style: italic; color: var(--muted); line-height: 10px; }
  .article p { margin-top: 8px; font-size: 7.9px; line-height: 14.2px; color: var(--text); }
  .rule { position: absolute; height: 1px; background: var(--rule); }

  .news-item { position: absolute; left: 493px; width: 190px; }
  .news-thumb { position: absolute; left: 0; top: 0; width: 41px; height: 41px; }
  .news-date { position: absolute; left: 0; top: 49px; width: 41px; height: 15px; background: var(--green); color: var(--white); font-size: 6px; font-weight: 700; text-align: center; line-height: 15px; }
  .news-date::before { content: ""; position: absolute; left: 17px; top: -4px; border: 4px solid transparent; border-top: 0; border-bottom-color: var(--green); }
  .news-item h3 { position: absolute; left: 53px; top: 0; font-size: 9px; font-weight: 500; color: var(--ink); white-space: nowrap; }
  .news-item p { position: absolute; left: 53px; top: 17px; width: 140px; font-size: 7.9px; line-height: 14.2px; color: var(--text); }

  /* Footer */
  .footer { position: absolute; left: 0; top: 1164px; width: 756px; height: 36px; background: var(--slate); color: var(--white); }
  .footer .copy { position: absolute; left: 74px; top: 13px; font-size: 7.6px; }
  .footer .flink { position: absolute; top: 13px; font-size: 7.6px; font-weight: 500; }
</style>
</head>
<body>
<div class="canvas">

  <header class="masthead">
    <svg class="abs" width="756" height="100" style="left:0;top:0" aria-hidden="true">
      <polygon points="0,0 287,0 0,255" fill="#e9e9eb"/>
    </svg>
    <div class="brand">BRIGHT REBOUNDS</div>
    <div class="share-link">SHARE YOUR STORY</div>
    <div class="field country">Select country
      <svg width="6" height="5" viewBox="0 0 6 5"><polygon points="0,0 6,0 3,5" fill="#666"/></svg>
    </div>
    <div class="field search">Search
      <svg width="8" height="8" viewBox="0 0 8 8"><circle cx="5" cy="3" r="2.3" fill="none" stroke="#999" stroke-width="1"/><line x1="3.3" y1="4.7" x2="0.8" y2="7.2" stroke="#999" stroke-width="1.2"/></svg>
    </div>

    <svg class="nav-bar" width="756" height="44" aria-hidden="true">
      <polygon points="245,0 756,0 756,44 201,44" fill="var(--green)"/>
    </svg>
    <nav>
      <span class="nav" style="left:285px">ABOUT US</span>
      <span class="nav" style="left:344px">PERSONAL STORIES</span>
      <span class="nav" style="left:441px">TIPS FOR LIVING</span>
      <span class="nav" style="left:523px">NEWS</span>
      <span class="nav" style="left:566px">RESOURCES</span>
      <span class="nav" style="left:632px">CONTACT US</span>
    </nav>

    <svg class="hero-photo" width="756" height="260" role="img" aria-label="Photo of three friends laughing together on a sofa with coffee and snacks">
      <defs>
        <linearGradient id="heroTone" x1="0" y1="0" x2="1" y2="1">
          <stop offset="0" stop-color="#c9b6a4"/>
          <stop offset="0.45" stop-color="#b79a86"/>
          <stop offset="1" stop-color="#8e7a70"/>
        </linearGradient>
      </defs>
      <polygon points="193,0 627,0 482,260 0,260" fill="url(#heroTone)"/>
    </svg>

    <div class="hero-copy">
      <div class="hero-title"><span class="accent">SHARING</span> STORIES<br>AND GIVING <span class="accent">HOPE</span></div>
      <p class="hero-text">to people around the world who<br>are facing inflammatory bowel<br>disease, colorectal cancer, or have<br>had ostomy surgery.</p>
    </div>
    <div class="btn" style="left:551px;width:53px">SHARE A STORY</div>
    <div class="or">or</div>
    <div class="btn" style="left:629px;width:53px">READ STORIES</div>
  </header>

  <section class="intro">
    <h1>Plan, make, achieve and enjoy your life!</h1>
    <div class="divider"></div>
    <p>Cum sociis natoque penatibus et magnis dis parturient montes, nascetur ridiculus mus. Sed posuere consectetur est at lobortis. Maecenas sed diam eget risus varius blandit sit amet non magna.</p>
  </section>

  <section class="about">
    <h2 class="heading" style="left:74px;top:541px">What is Bright Rebounds</h2>
    <p class="body" style="left:74px;top:578px;width:185px">Duis mollis, est non commodo luctus, nisi porttitor ligula, eget lacinia odio sem nec elit. Aenean eu leo quam. Pellentesque ornare sem lacinia quam. Aenean lacinia bibendum nulla sed consectetur. Nulla vitae elit libero, a pharetra augue. Phasellus turpis diam, dictum vitae venenatis non, mattis et nisl.</p>
    <p class="body" style="left:74px;top:692px;width:185px">In a nibh enim, vitae condimentum tellus. Aliquam tincidunt odio eu lectus scelerisque ut luctus sem cursus. Aliquam elementum, lacus id egestas aliquet, quam elit dapibus massa, at auctor tortor ante ut lacus. Aliquam tincidunt dictum lacinia. Donec risus eros, congue et lobortis ac, mattis nec neque.</p>
  </section>

  <section class="share">
    <h2 class="heading" style="left:285px;top:541px">Share a story</h2>
    <p class="body" style="left:285px;top:578px;width:397px">Duis mollis, est non commodo luctus, nisi porttitor ligula, eget lacinia odio sem nec elit. Aenean eu leo quam. Pellentesque ornare sem lacinia quam. Aenean lacinia bibendum nulla sed consectetur. Nulla vitae elit libero, a pharetra augue. Phasellus turpis diam, dictum vitae venenatis.</p>
    <a class="link-green" style="left:581px;top:628px">Share your story</a>
    <h3 class="subhead" style="left:284px;top:643px">Featured stories</h3>

    <svg class="photo" style="left:285px;top:669px" width="186" height="92" role="img" aria-label="Portrait of a smiling man in front of a brick wall">
      <rect width="186" height="92" fill="#9a6a50"/>
    </svg>
    <div class="story-name" style="left:284px;top:765px">Ned Calloway<span>Adelaida</span></div>

    <svg class="photo" style="left:494px;top:669px" width="187" height="92" role="img" aria-label="Photo of a woman and a uniformed officer standing together">
      <rect width="187" height="92" fill="#4a3a2a"/>
      <circle cx="170" cy="79" r="5" fill="#d8d8d8"/>
      <polygon points="168,76 168,82 173,79" fill="#4a3a2a"/>
    </svg>
    <div class="story-name" style="left:493px;top:765px">Marisa Dunmore<span>Melburne</span></div>
    <div class="more">MORE STORIES</div>
  </section>

  <section class="tips">
    <h2 class="heading" style="left:74px;top:832px">Tips for living</h2>
    <p class="body" style="left:74px;top:869px;width:395px">Duis mollis, est non commodo luctus, nisi porttitor ligula, eget lacinia odio sem nec elit. Aenean eu leo quam. Pellentesque ornare sem lacinia quam. Aenean lacinia bibendum nulla sed consectetur. Nulla vitae elit libero, a pharetra augue. Phasellus turpis diam, dictum vitae venenatis non, mattis et nisl. In a nibh enim, vitae condimentum tellus. Aliquam tincidunt odio eu lectus scelerisque ut luctus sem cursus.</p>

    <article class="article" style="left:73px;top:943px">
      <h3>Finding Intimacy</h3>
      <div class="byline">by Hannah Selwyn</div>
      <p>Your ostomy doesn’t have to inhibit your love life. You can have an exciting, meaningful and fulfilling relationship. Here’s how.</p>
    </article>
    <article class="article" style="left:283px;top:943px">
      <h3>No Guts, Still Glory</h3>
      <div class="byline">by Clara Whitfield Hayes</div>
      <p>When asked what he thought this article should be titled, former football standout and S-pouch surgery alum Owen Brasher didn’t hesitate...</p>
    </article>
    <div class="rule" style="left:74px;top:1029px;width:126px"></div>
    <div class="rule" style="left:283px;top:1029px;width:126px"></div>
    <article class="article" style="left:73px;top:1042px">
      <h3>Food, Glorious Food!</h3>
      <div class="byline">by Dana Roussel, RD</div>
      <p>Whether it’s the turkey at Thanksgiving, potato pancakes at Hanukkah, or jambalaya for Kwanzaa, you can enjoy the season’s foods despite ostomy.</p>
    </article>
    <article class="article" style="left:283px;top:1042px">
      <h3>Triumphs &amp; Inspiration: Marathon Man</h3>
      <div class="byline">by Irene Caldwell</div>
      <p>Despite serious setbacks, former wrestler and J-pouch surgery survivor Leo Tarrant fought his way back happiness, one step at a time.</p>
    </article>
  </section>

  <section class="news">
    <h2 class="heading" style="left:493px;top:832px">Latest news</h2>

    <div class="news-item" style="top:873px">
      <svg class="news-thumb" role="img" aria-label="News thumbnail of glassware on a table"><rect width="41" height="41" fill="#6e4a3c"/></svg>
      <div class="news-date">04 APR</div>
      <h3>Vestibulum turpis libero</h3>
      <p>Praesent commodo cursus magna, Maecenas faucibus mollis interdum. Praesent commodo cursus magna,</p>
    </div>
    <div class="rule" style="left:502px;top:952px;width:170px"></div>

    <div class="news-item" style="top:968px">
      <svg class="news-thumb" role="img" aria-label="News thumbnail of a runner in a race"><rect width="41" height="41" fill="#8a9bb0"/></svg>
      <div class="news-date">14 MAR</div>
      <h3>Fringilla Venenatis Cursus</h3>
      <p>Etiam porta sem malesuada magna mollis euismod. Donec ullamcorper nulla non metus auctor fringilla.</p>
    </div>
    <div class="rule" style="left:502px;top:1047px;width:170px"></div>

    <div class="news-item" style="top:1062px">
      <svg class="news-thumb" role="img" aria-label="News thumbnail portrait of a woman"><rect width="41" height="41" fill="#b58a6e"/></svg>
      <div class="news-date">02 FEB</div>
      <h3>Vivamus antero convallis</h3>
      <p>Etiam porta sem malesuada magna mollis euismod. Donec ullamcorper nulla non metus auctor fringilla.</p>
    </div>
  </section>

  <footer class="footer">
    <div class="copy">Copyright by Bright Rebounds 2014</div>
    <a class="flink" style="left:491px">LEGAL NOTICE</a>
    <a class="flink" style="left:565px">PRIVACY POLICY</a>
    <a class="flink" style="left:647px">SITEMAP</a>
  </footer>

</div>
</body>
</html>
```